Tech Startup Needs Business Card Design

I am looking for an eye catching business card design for our new company, Blue Kettle. We are a place for business owners and contractors to share their experiences with their customers and check their current customers. Our website, www.blue-kettle.example, may be able to offer some guidance as to the design.

Industry/Entity Type

Business

Contact Information for Business Card

Tom Varrowby
888-555-0147
Tom@blue-kettle.example
www.blue-kettle.example

```html
<!DOCTYPE html>
<html lang="en">
<head>
<meta charset="utf-8">
<title>Blue Kettle – Business Card</title>
<link href="https://fonts.googleapis.com/css2?family=Roboto:wght@400;500;700&display=swap" rel="stylesheet">
<style>
  :root {
    --brand-red: #ee1c25;
    --ink: #111111;
    --muted: #555555;
    --paper: #ffffff;
    --stage: #ecebe8;
    --tint: #fbe3e4;
  }
  * { margin: 0; padding: 0; box-sizing: border-box; }
  html, body {
    width: 1200px; height: 950px; overflow: hidden;
    background: var(--stage);
    font-family: "Roboto", Arial, sans-serif;
  }
  .sheet {
    position: relative; width: 1200px; height: 950px;
  }
  .card {
    position: absolute; left: 250px;
    width: 700px; height: 400px;
    border-radius: 26px; overflow: hidden;
    box-shadow: 0 10px 26px rgba(0,0,0,.18);
  }
  /* Front */
  .card--front { top: 45px; background: var(--brand-red); }
  .front-brand {
    position: absolute; left: 0; right: 0; top: 150px;
    display: flex; align-items: center; justify-content: center; gap: 16px;
    color: var(--paper); font-weight: 500; font-size: 50px; letter-spacing: .5px;
  }
  .front-brand .dot {
    width: 30px; height: 30px; border-radius: 50%; background: var(--paper);
  }
  /* Back */
  .card--back { top: 505px; background: var(--paper); }
  .side-band {
    position: absolute; left: 0; top: 0; bottom: 0; width: 64px;
    background: var(--brand-red);
  }
  .faint-mark {
    position: absolute; right: 40px; bottom: -60px;
    width: 300px; height: 300px; border-radius: 50%;
    background: var(--tint);
  }
  .wordmark {
    position: absolute; left: 92px; top: 40px;
    display: flex; align-items: center; gap: 14px;
    color: var(--ink); font-weight: 500; font-size: 62px; letter-spacing: -.5px;
  }
  .wordmark .dot {
    width: 34px; height: 34px; border-radius: 50%; background: var(--brand-red);
  }
  .holder { position: absolute; left: 92px; top: 168px; }
  .holder-name { color: var(--brand-red); font-weight: 700; font-size: 25px; }
  .holder-role { color: var(--ink); font-size: 17px; margin-top: 4px; }
  .contacts {
    position: absolute; left: 92px; top: 248px;
    list-style: none; display: grid; gap: 9px;
  }
  .contacts li {
    display: flex; align-items: center; gap: 12px;
    color: var(--muted); font-size: 17px;
  }
  .contacts svg { width: 18px; height: 18px; flex: none; }
</style>
</head>
<body>
<main class="sheet">
  <section class="card card--front" aria-label="Card front">
    <div class="front-brand"><span class="dot"></span><span>blue kettle</span></div>
  </section>

  <section class="card card--back" aria-label="Card back">
    <div class="side-band"></div>
    <div class="faint-mark"></div>
    <div class="wordmark"><span class="dot"></span><span>bluekettle</span></div>
    <div class="holder">
      <p class="holder-name">Tom Varrowby</p>
      <p class="holder-role">President</p>
    </div>
    <ul class="contacts">
      <li>
        <svg viewBox="0 0 24 24" aria-hidden="true"><path fill="#ee1c25" d="M6.6 10.8a15.1 15.1 0 0 0 6.6 6.6l2.2-2.2c.3-.3.7-.4 1-.2 1.1.4 2.3.6 3.6.6.6 0 1 .4 1 1V20c0 .6-.4 1-1 1A17 17 0 0 1 3 4c0-.6.4-1 1-1h3.5c.6 0 1 .4 1 1 0 1.3.2 2.5.6 3.6.1.3 0 .7-.2 1z"/></svg>
        888-555-0147
      </li>
      <li>
        <svg viewBox="0 0 24 24" aria-hidden="true"><rect x="2" y="5" width="20" height="14" rx="2" fill="#ee1c25"/><path d="M3 6l9 7 9-7" fill="none" stroke="#fff" stroke-width="1.8"/></svg>
        Tom@blue-kettle.example
      </li>
      <li>
        <svg viewBox="0 0 24 24" aria-hidden="true"><circle cx="12" cy="12" r="10" fill="#ee1c25"/><path d="M2.5 12h19M12 2.5c3 3 3 16 0 19M12 2.5c-3 3-3 16 0 19" fill="none" stroke="#fff" stroke-width="1.4"/></svg>
        www.blue-kettle.example
      </li>
    </ul>
  </section>
</main>
</body>
</html>
```